Advertisement Design Project: Print Ad

I need a print ad for a local boutique ski shop.
Size 5.43 inches wide by 5 inches high
full color
I am looking for a couple of options to market the following:
A: Kids Ski seasonal rental package
and/or
B:Early Season sales promotion
idea 1: "Be the first to check out this season's gear"
idea 2: "Looks you can take from the slopes to the streets"
idea 3: "The newer your gear, the better the performance"
idea 4: "Start off the new year with new gear"
OR YOUR COPY SUGGESTIONS
We would like a photo in the ad as well.
Need to include:
Our Name: Tarvell Ski Shop
Our address: 2847 N Marrow Lane, 3 blocks South of Cresthaven Commons in Quillstone Plaza
Target Market(s)
Families and Sports enthusiasts
Industry/Entity Type
Boutique
Look and feel

```html
<!DOCTYPE html>
<html lang="en">
<head>
<meta charset="utf-8">
<title>Tarvell Ski Shop – Print Ad</title>
<link rel="stylesheet" href="https://fonts.googleapis.com/css2?family=Roboto+Condensed:wght@400;700&family=Arimo:wght@400&display=swap">
<style>
  :root {
    --backdrop: #1c1c1c;
    --sky-deep: #1d3a86;
    --sky-mid: #2a5db0;
    --sky-light: #3a86c4;
    --snow-shade: #b9c6dc;
    --snow-light: #e6ecf5;
    --snow-bright: #f4f6fa;
    --suit-red: #d8383c;
    --ski-grey: #a9b3c4;
    --brand-red: #c8202a;
    --headline-white: #ffffff;
    --address-ink: #111111;
  }
  * { margin: 0; padding: 0; box-sizing: border-box; }
  html, body {
    width: 1200px;
    height: 900px;
    overflow: hidden;
    background: var(--backdrop);
  }
  .ad {
    position: absolute;
    left: 295px;
    top: 27px;
    width: 623px;
    height: 831px;
    overflow: hidden;
  }
  .ad__scene {
    position: absolute;
    inset: 0;
    background: linear-gradient(
      180deg,
      var(--sky-deep) 0%,
      var(--sky-mid) 35%,
      var(--sky-light) 55%,
      var(--snow-light) 57%,
      var(--snow-shade) 75%,
      var(--snow-shade) 100%
    );
  }
  .ad__snow-lip {
    position: absolute;
    left: -40px;
    top: 690px;
    width: 330px;
    height: 220px;
    border-radius: 50% 50% 0 0;
    background: linear-gradient(180deg, var(--snow-bright), var(--snow-light));
    transform: rotate(18deg);
  }
  .ad__skier {
    position: absolute;
    left: 0;
    top: 58px;
    width: 365px;
    height: 495px;
    border-radius: 40% 30% 45% 20%;
    background: linear-gradient(
      155deg,
      var(--ski-grey) 0%,
      var(--suit-red) 40%,
      var(--suit-red) 55%,
      var(--ski-grey) 100%
    );
    opacity: 0.55;
  }
  .ad__headline {
    position: absolute;
    right: 30px;
    top: 228px;
    text-align: right;
    font-family: "Roboto Condensed", sans-serif;
    font-weight: 400;
    font-size: 63px;
    line-height: 60px;
    color: var(--headline-white);
    text-transform: uppercase;
    transform: scaleX(0.87);
    transform-origin: right top;
  }
  .ad__headline em {
    font-style: normal;
    font-weight: 700;
    color: var(--brand-red);
  }
  .ad__brand {
    position: absolute;
    right: 46px;
    top: 612px;
    font-family: "Roboto Condensed", sans-serif;
    font-weight: 700;
    font-size: 141px;
    line-height: 1;
    color: var(--brand-red);
  }
  .ad__tagline {
    position: absolute;
    right: 38px;
    top: 747px;
    font-family: "Roboto Condensed", sans-serif;
    font-weight: 400;
    font-size: 26px;
    line-height: 1;
    letter-spacing: 8px;
    color: var(--headline-white);
    white-space: nowrap;
  }
  .ad__address {
    position: absolute;
    left: 31px;
    top: 796px;
    font-family: "Arimo", sans-serif;
    font-size: 15px;
    color: var(--address-ink);
    white-space: nowrap;
  }
</style>
</head>
<body>
  <main class="ad">
    <div class="ad__scene" role="img" aria-label="Photo background of a deep blue winter sky above a groomed snow halfpipe"></div>
    <div class="ad__snow-lip"></div>
    <div class="ad__skier" role="img" aria-label="Photo of a freestyle skier in a red suit and green helmet mid-jump with skis crossed"></div>
    <h1 class="ad__headline">
      The <em>Newer</em><br>
      Your Gear,<br>
      The <em>Better</em> Your<br>
      Performance
    </h1>
    <div class="ad__brand">Tarvell</div>
    <div class="ad__tagline">SKI + SPORT</div>
    <p class="ad__address">2847 N Marrow Lane, 3 blocks South of Cresthaven Commons in Quillstone Plaza</p>
  </main>
</body>
</html>
```